A4 Tri-fold Brochure for Sedation Dentist Specialist Dr. Marlon and Sedation Dentistry.

I would like to create an A4 tri-fold brochure for our Dental Sedation Specialist Dr. Marlon Vesk. Please carefully select the most suitable highlights from his bio below.

This brochure has two parts. Highlighting what makes Dr. Marlon Vesk unique and trustworthy. Include a picture of him (attached). The second part is about sedation dentistry. All you need to know here: http://www.calmchairplex.com/how-does-sedation-dentistry-work

Avoid making it too wordy.

Meet Dr. Roh Dak Marlon Vesk, DDS

Inspired to Become a Dentist:
As a child, Dr. Marlon Vesk always felt stressed whenever he had to see a dentist. He knew that he wanted to become a dentist to help put patients completely at ease while they experienced quality dental care.

He is passionate about giving patients the healthy, beautiful smiles they deserve. “I find it fulfilling when I can see my patients’ beautiful smiles and how they can finally appreciate the joy of eating with a healthy set of teeth. However, what I love most about my job is the ability to provide a stress-free and comfortable experience at the dentist’s office, particularly for children, through sedation and general anesthesia.”

Educational Achievements:
Before becoming a dentist, Dr. Marlon Vesk earned his undergraduate degree at the Pellridge University of Northern Basin where he received a Bachelor of Medical Science Honor Specialization degree with distinction in biochemistry. He then completed his Doctor of Dental Surgery degree with honors at the Harwick Crest University. While there, he received the Elmer Drayce Medal in his class for outstanding achievement in anesthesia. He then pursued his three-year residency as well as a master’s degree in dental anesthesia at the Harwick Crest University.

So he can provide his patients with the latest in dentistry, Dr. Marlon Vesk enjoys pursuing additional knowledge, particularly in the areas of dental anesthesia as well as advanced technologies in dentistry. He is currently part of the Molar Horizon Circle study club and has enrolled in the Core Rootwork Mini- Residency Program. He also serves as a clinical instructor at the Plenvo Center at the Harwick Crest University.

Association Memberships:
In addition to his academic credentials, Dr. Marlon Vesk is a member of several associations:
The Vantley Board of Dental Surgeons of Quarrow (VBDSQ)
Dental Norvane Guild of Dental Anesthesia (NGDA)
Brisken Forum of Dental Anesthesia (BFDA)
Quarrow Dental Federation (QDF)
Outside the Practice

When he’s not at the practice, Dr. Marlon Vesk enjoys spending time with his wife Wren and their two poodles Pippa and Biscuit, who are spoiled rotten! “Wren and I love taking our dogs out on hikes and to the dog park on weekends. I also enjoy a wide range of activities from model building and playing the piano to soccer, gym and archery.” He stays fit by working out at the local Fitwell gym, and he likes to walk in Ashbury Lake Park and Dunmore Field Park.

Dr. Marlon Vesk considers himself to be a kid at heart. He is a big fan of superheroes and animated movies. “I get really excited about any upcoming superhero or Zentry Lumo movies. Till this day, I still collect superhero toy figures.”

He supports the BrightCot Foundation as well as the Quarrow League for the Protection of Animal Welfare (LPAW).

Experience outstanding dental care with our highly skilled dentist. Contact us today to schedule an appointment with Dr. Marlon Vesk! He speaks English, Cantonese, and Mandarin.

Target Market(s)

Mothers with young kids.

Industry/Entity Type

Dental

Font styles to use
Sans Serif

Requirements
Should not have
• Prices

```html
<!DOCTYPE html>
<html lang="en">
<head>
<meta charset="utf-8">
<title>A4 Tri-fold Brochure – Dr. Marlon Vesk</title>
<link href="https://fonts.googleapis.com/css2?family=Open+Sans:wght@700&family=PT+Sans:wght@400;700&family=Signika:wght@400;600&display=swap" rel="stylesheet">
<style>
:root{
  --ink:#111;
  --yellow:#f3e66a;
  --cream:#fff6c8;
  --white:#ffffff;
  --box-dark:rgba(18,38,52,.72);
  --box-green:rgba(22,60,30,.72);
  --box-brown:rgba(95,52,10,.62);
  --green-band:#8dbb3a;
  --orange-title:#fff1a0;
  --item-title:#fff08a;
}
*{box-sizing:border-box;margin:0;padding:0}
html,body{width:1200px;height:1200px;overflow:hidden;background:#fff}
.canvas{position:relative;width:1200px;height:1200px;font-family:"PT Sans",sans-serif;color:var(--ink)}
.sheet-title{position:absolute;left:0;top:86px;width:236px;text-align:center;font:700 35px/46px "Open Sans",sans-serif}
.panel-label{position:absolute;font:700 28px/1 "Open Sans",sans-serif;text-align:center;width:240px}
.sheet{position:absolute;left:250px;width:700px;height:495px;overflow:hidden}
.sheet-outside{top:90px;background:linear-gradient(100deg,#2f8a3a 0%,#7fa51f 22%,#c08a1a 38%,#d0821c 52%,#b8a032 64%,#2f6f74 72%,#1f4f78 88%,#2b3f6e 100%)}
.sheet-inside{top:678px;background:linear-gradient(100deg,#1d3f6e 0%,#1f5a76 30%,#2d7a6c 48%,#568d52 62%,#2d6a6c 66%,#c9801c 66.1%,#d68a22 80%,#c7761a 100%)}
.box{position:absolute;color:var(--yellow);font-family:"Signika",sans-serif;text-align:center;display:flex;align-items:center;justify-content:center}
.box-green{background:var(--box-green)}
.box-dark{background:var(--box-dark)}
.box-brown{background:var(--box-brown);color:var(--white);font:600 9px "PT Sans",sans-serif;letter-spacing:.2px}
.heading{font-size:19px;line-height:24px;font-weight:600}
.copy{position:absolute;color:var(--white);font-size:7.6px;line-height:10px}
.copy p+p{margin-top:10px}
.copy-flap{font-size:9.2px;line-height:12px}
.copy-flap p+p{margin-top:12px}
.map{position:absolute;left:16px;top:30px;width:150px;height:240px;background:linear-gradient(160deg,rgba(190,150,40,.35),rgba(150,110,20,.35))}
.address{position:absolute;left:0;width:100%;text-align:center;color:var(--white);font:700 10.5px/13px "PT Sans",sans-serif}
.brand{position:absolute;text-align:center;color:var(--white);font:400 10px "PT Sans",sans-serif;letter-spacing:.5px;width:180px}
.brand-dot{display:block;margin:0 auto 8px;width:34px;height:34px;border:2px solid var(--white);border-radius:50%}
.contact{position:absolute;text-align:center;color:var(--white);font:700 16px "PT Sans",sans-serif;width:233px}
.portrait{position:absolute;left:46px;top:20px;width:154px;height:256px;background:#fff;padding:6px}
.portrait span{display:block;width:100%;height:100%;background:linear-gradient(180deg,#23486a,#1a3552 60%,#122233)}
.name{position:absolute;left:0;width:100%;text-align:center;color:var(--white);font-family:"PT Sans",sans-serif}
.photo-full{position:absolute;left:210px;top:170px;width:136px;height:325px;background:linear-gradient(180deg,rgba(40,60,80,.0),rgba(35,55,85,.55) 30%,rgba(24,38,70,.8))}
.band{position:absolute;left:462px;top:0;width:238px;height:62px;background:var(--green-band);text-align:center;color:var(--orange-title);font-family:"Signika",sans-serif}
.band small{display:block;padding-top:15px;font:700 7.2px "PT Sans",sans-serif;color:var(--yellow)}
.band b{display:block;font-size:16px;font-weight:600;color:var(--orange-title)}
.item{position:absolute;left:466px;width:230px;display:flex;gap:8px;color:var(--white)}
.item svg{flex:0 0 30px}
.item h4{font:italic 700 7px "PT Sans",sans-serif;color:var(--item-title);margin-bottom:2px}
.item p{font-size:5.8px;line-height:7.8px}
</style>
</head>
<body>
<div class="canvas">
  <h1 class="sheet-title">A4 Tri-fold<br>Brochure<br>(Flat Layout)</h1>

  <div class="panel-label" style="left:255px;top:50px">FLAP</div>
  <div class="panel-label" style="left:471px;top:50px">BACK</div>
  <div class="panel-label" style="left:708px;top:50px">FRONT</div>

  <section class="sheet sheet-outside">
    <!-- Flap -->
    <div class="box box-green heading" style="left:24px;top:0;width:182px;height:104px">Inspired<br>to Become<br>a Dentist</div>
    <div class="copy copy-flap" style="left:43px;top:136px;width:148px">
      <p>As a child, Dr. Marlon Vesk always felt stressed whenever he had to see a dentist. He knew that he wanted to become a dentist to help put patients completely at ease while they experienced quality dental care.</p>
      <p>He is passionate about giving patients the healthy, beautiful smiles they deserve. “I find it fulfilling when I can see my patients’ beautiful smiles and how they can finally appreciate the joy of eating with a healthy set of teeth.</p>
      <p>However, what I love most about my job is the ability to provide a stress-free and comfortable experience at the dentist’s office, particularly for children, through sedation and general anesthesia.”</p>
    </div>

    <!-- Back -->
    <div class="box box-dark" style="left:255px;top:0;width:182px;height:327px;display:block">
      <div class="map" role="img" aria-label="Street map showing the route to the dental clinic"></div>
      <div class="address" style="top:298px">1234 Corlan St., Suite 709<br>Harwick, Quarrow Q4P 1E4</div>
    </div>
    <div class="brand" style="left:256px;top:382px"><span class="brand-dot"></span>DENTAL CLINIC</div>
    <div class="contact" style="left:230px;top:449px">www.velmora-dental.com</div>

    <!-- Front -->
    <div class="box box-dark" style="left:495px;top:0;width:182px;height:327px;display:block">
      <div class="portrait" style="left:13px;top:20px" role="img" aria-label="Portrait photo of Dr. Marlon Vesk in dark scrubs with a stethoscope"><span></span></div>
      <div class="name" style="top:288px;font-size:14px;font-weight:700">Dr. Marlon Vesk</div>
      <div class="name" style="top:305px;font-size:9px;font-weight:700">Dental Sedation Specialist</div>
    </div>
    <div class="brand" style="left:500px;top:382px"><span class="brand-dot"></span>DENTAL CLINIC</div>
    <div class="contact" style="left:467px;top:449px">(02) 555.0148</div>
  </section>

  <div class="panel-label" style="left:244px;top:636px">INSIDE LEFT</div>
  <div class="panel-label" style="left:478px;top:636px">INSIDE CENTER</div>
  <div class="panel-label" style="left:710px;top:636px">INSIDE RIGHT</div>

  <section class="sheet sheet-inside">
    <!-- Inside left -->
    <div class="box box-dark heading" style="left:24px;top:0;width:182px;height:62px">Educational<br>Achievements</div>
    <div class="copy" style="left:27px;top:78px;width:184px">
      <p>Before becoming a dentist, Dr. Marlon Vesk earned his undergraduate degree at the Pellridge University of Northern Basin where he received a Bachelor of Medical Science Honor Specialization degree with distinction in biochemistry.</p>
      <p>He then completed his Doctor of Dental Surgery degree with honors at the Harwick Crest University. While there, he received the Elmer Drayce Medal in his class for outstanding achievement in anesthesia. He then pursued his three-year residency as well as a master’s degree in dental anesthesia at the Harwick Crest University.</p>
      <p>He is currently part of the Molar Horizon Circle study club and has enrolled in the Core Rootwork Mini-Residency Program. He also serves as a clinical instructor at the Plenvo Center at the Harwick Crest University.</p>
    </div>
    <div class="box box-dark heading" style="left:24px;top:288px;width:182px;height:62px">Association<br>Memberships</div>
    <div class="copy" style="left:27px;top:370px;width:184px">
      <p>In addition to his academic credentials, Dr. Marlon Vesk is a member of several associations:<br>
      • The Vantley Board of Dental Surgeons of Quarrow (VBDSQ)<br>
      • Dental Norvane Guild of Dental Anesthesia (NGDA)<br>
      • Brisken Forum of Dental Anesthesia (BFDA)<br>
      • Quarrow Dental Federation (QDF)</p>
    </div>

    <!-- Inside center -->
    <div class="box box-dark heading" style="left:252px;top:0;width:184px;height:62px">Outside<br>the Practice</div>
    <div class="copy" style="left:256px;top:78px;width:182px">
      <p>When he’s not at the practice, Dr. Marlon Vesk enjoys spending time with his wife Wren and their two poodles Pippa and Biscuit, who are spoiled rotten! “Wren and I love taking our dogs out on hikes and to the dog park on weekends. I also enjoy a wide range of activities from model building and playing the piano to soccer, gym and archery.” He stays fit by working out at the local Fitwell gym, and he likes to walk in Ashbury Lake Park and Dunmore Field Park.</p>
    </div>
    <div class="photo-full" role="img" aria-label="Photo of Dr. Marlon Vesk smiling in navy scrubs with a stethoscope"></div>
    <div class="copy" style="left:346px;top:184px;width:94px">
      <p>Dr. Marlon Vesk considers himself to be a kid at heart. He is a big fan of superheroes and animated movies. “I get really excited about any upcoming superhero or Zentry Lumo movies. Till this day, I still collect superhero toy figures.”</p>
      <p>He supports the BrightCot Foundation as well as the Quarrow League for the Protection of Animal Welfare (LPAW).</p>
      <p>Experience outstanding dental care with our highly skilled dentist. Contact us today to schedule an appointment with Dr. Marlon Vesk! He speaks English, Cantonese, and Mandarin.</p>
    </div>

    <!-- Inside right -->
    <div class="band"><small>RELAXING IN THE DENTIST’S CHAIR WITH</small><b>SEDATION DENTISTRY</b></div>
    <div class="box box-brown" style="left:478px;top:64px;width:206px;height:28px">BENEFITS OF SEDATION DENTISTRY</div>

    <div class="item" style="top:104px">
      <svg width="30" height="30" viewBox="0 0 30 30" fill="none" stroke="#fff" stroke-width="2.4"><circle cx="15" cy="15" r="12"/><path d="M15 8v7h6"/></svg>
      <div><h4>TIME</h4><p>Dental sedation can make it feel like less time has passed. Ideal if you need to get a lot of dental work done.</p></div>
    </div>
    <div class="item" style="top:150px">
      <svg width="30" height="30" viewBox="0 0 30 30" fill="none" stroke="#fff" stroke-width="2.2"><circle cx="17" cy="9" r="6"/><circle cx="11" cy="20" r="4"/><path d="M13 13l-8 12"/></svg>
      <div><h4>CONVENIENCE</h4><p>If you need a great deal of work, you can get more accomplished in one visit. Reduces the need for multiple visits to the dentist.</p></div>
    </div>
    <div class="item" style="top:198px">
      <svg width="30" height="30" viewBox="0 0 30 30" fill="#fff"><path d="M2 13c6-3 9-2 13 0 4-2 7-3 13 0-4 8-22 8-26 0z"/></svg>
      <div><h4>COMFORT</h4><p>Sedation allows you to relax during dental treatments. Especially important if you have anxieties or fears about going to the dentist.</p></div>
    </div>
    <div class="item" style="top:246px">
      <svg width="30" height="30" viewBox="0 0 30 30"><circle cx="15" cy="15" r="13" fill="#fff"/><path d="M12 7h6v5h5v6h-5v5h-6v-5H7v-6h5z" fill="#c97a1a"/></svg>
      <div><h4>HEALTH</h4><p>When you’re not afraid of the dentist, you’re more likely to go regularly. Helps keep your oral health in good standing since you won’t avoid visits.</p></div>
    </div>

    <div class="box box-brown" style="left:478px;top:289px;width:206px;height:28px">TYPES OF DENTAL SEDATION</div>

    <div class="item" style="top:328px">
      <svg width="30" height="30" viewBox="0 0 30 30" fill="#fff"><rect x="9" y="8" width="11" height="21" rx="4"/><rect x="12" y="2" width="5" height="6"/><path d="M17 4h8v3" stroke="#fff" stroke-width="2" fill="none"/></svg>
      <div><h4>NITROUS OXIDE (LAUGHING GAS)</h4><p>Your dentist gives you a mask and you breathe in nitrous oxide. Helps you feel more relaxed, and wears off quickly. Sometimes used in combination with other methods.</p></div>
    </div>
    <div class="item" style="top:380px">
      <svg width="30" height="30" viewBox="0 0 30 30" fill="#fff"><rect x="4" y="6" width="9" height="18" rx="4.5" transform="rotate(-40 8 15)"/><circle cx="21" cy="21" r="6"/></svg>
      <div><h4>ORAL CONSCIOUS</h4><p>A popular and effective method of sedation dentistry. You’ll take a pill, and the dental work only begins once it’s taken effect. Even though you’re sedated, you’ll be able to respond to questions.</p></div>
    </div>
    <div class="item" style="top:434px">
      <svg width="30" height="30" viewBox="0 0 30 30" fill="#fff"><rect x="8" y="2" width="14" height="18" rx="3"/><rect x="13" y="20" width="4" height="5"/><path d="M15 25v4" stroke="#fff" stroke-width="2"/></svg>
      <div><h4>INTRAVENOUS (IV)</h4><p>Sedative is administered intravenously, giving you a precise level of relaxation. Performed by Board Certified Anesthesiologist. Depending on the procedure, you may be sedated to different levels.</p></div>
    </div>
  </section>
</div>
</body>
</html>
```